Letterhead for Dane Holloway

I need a letterhead based on the business card design

Industry/Entity Type

Business

Requirements
Must have
• Footer: Dane Holloway Naturopath
Shop 3042c, 451 Marrow Lane, Sydney 2000

```html
<!DOCTYPE html>
<html lang="en">
<head>
<meta charset="utf-8">
<title>Dane Holloway Naturopath – Letterhead</title>
<link href="https://fonts.googleapis.com/css2?family=Questrial&display=swap" rel="stylesheet">
<style>
  :root {
    --orange: #ff6a00;
    --orange-mid: #ff9a45;
    --orange-soft: #ffc795;
    --orange-text: #f7941d;
    --cream: #fff6ee;
    --paper: #ffffff;
    --ink: #333333;
  }
  * { margin: 0; padding: 0; box-sizing: border-box; }
  html, body {
    width: 900px;
    height: 1200px;
    overflow: hidden;
    background: var(--paper);
  }
  .letterhead {
    position: relative;
    width: 900px;
    height: 1200px;
    background: var(--paper);
    font-family: "Questrial", "Century Gothic", sans-serif;
    color: var(--ink);
    overflow: hidden;
  }
  .masthead {
    position: absolute;
    left: 0; top: 0;
    width: 900px;
    height: 161px;
    background: linear-gradient(90deg,
      var(--orange) 0%,
      #ff7410 30%,
      var(--orange-mid) 52%,
      var(--orange-soft) 70%,
      var(--cream) 90%,
      var(--paper) 100%);
  }
  .brand-name {
    position: absolute;
    left: 51px;
    top: 52px;
    font-size: 27px;
    letter-spacing: 0.5px;
    color: var(--paper);
    text-transform: uppercase;
  }
  .masthead-rule {
    position: absolute;
    left: 51px;
    right: 15px;
    top: 98px;
    height: 1.5px;
    background: linear-gradient(90deg, rgba(255,255,255,0.95), rgba(255,255,255,0.7));
  }
  .contact {
    position: absolute;
    right: 50px;
    top: 64px;
    text-align: right;
    font-size: 12.5px;
    line-height: 15px;
    color: var(--orange);
  }
  .contact-line {
    display: flex;
    justify-content: flex-end;
    align-items: center;
    gap: 5px;
  }
  .contact-icon { width: 10px; height: 10px; }
  .letter-date {
    position: absolute;
    right: 102px;
    top: 238px;
    font-size: 12.5px;
  }
  .letter-body {
    position: absolute;
    left: 108px;
    top: 296px;
    width: 686px;
    font-size: 12.5px;
    line-height: 19px;
  }
  .salutation { margin-bottom: 19px; }
  .letter-body p { margin-bottom: 19px; }
  .letter-body p.run-on { margin-top: -19px; }
  .signature { margin-top: 38px; }
  .leaf-art {
    position: absolute;
    right: 0;
    bottom: 0;
    width: 468px;
    height: 165px;
  }
  .footer-address {
    position: absolute;
    left: 51px;
    top: 1158px;
    font-size: 12.5px;
    color: var(--orange-text);
  }
</style>
</head>
<body>
<div class="letterhead">
  <header class="masthead">
    <div class="brand-name">Dane Holloway</div>
    <div class="masthead-rule"></div>
    <div class="contact">
      <div class="contact-line">
        <span>0431 552 806</span>
        <svg class="contact-icon" viewBox="0 0 10 10" aria-hidden="true">
          <rect x="2.5" y="0.5" width="5" height="9" rx="1" fill="none" stroke="#ff6a00" stroke-width="1"/>
          <rect x="4" y="7.3" width="2" height="0.9" fill="#ff6a00"/>
        </svg>
      </div>
      <div class="contact-line">
        <span>dhnaturopath@inbox.com.au</span>
        <svg class="contact-icon" viewBox="0 0 10 10" aria-hidden="true">
          <rect x="0.5" y="2" width="9" height="6" fill="#ff9a45"/>
          <path d="M0.8 2.3 L5 5.5 L9.2 2.3" fill="none" stroke="#ffffff" stroke-width="0.9"/>
        </svg>
      </div>
    </div>
  </header>

  <div class="letter-date">5 May 2014</div>

  <main class="letter-body">
    <div class="salutation">Dear Marcus</div>
    <p>Thank you for visiting the clinic last week. As we discussed, I have put together a gentle plan to support your energy, sleep and digestion over the coming months. The plan begins with small changes to your daily meals, adding more leafy greens, whole grains and fresh water while easing back on sugar and late coffee. I have also included a herbal tonic to take each morning, along with notes on dosage and timing. Please keep a short diary of how you feel each day so we can review your progress together and adjust anything that does not suit you.</p>
    <p>Your next appointment is booked for the first week of June. Before then, I would like you to try the breathing routine we practised and to walk outside for twenty minutes on most days. Rest and fresh air matter as much as any remedy.</p>
    <p class="run-on">If you notice any change you are unsure about, please call the clinic and we will find a time to talk it through with you.</p>
    <p>I have enclosed a copy of your plan, a list of suggested foods and a small sample of the tea blend. Take your time reading through it all, and bring any questions to our next visit. I look forward to hearing how you are feeling and to working with you as your health continues to improve.</p>
    <div class="signature">Dane Holloway</div>
  </main>

  <svg class="leaf-art" viewBox="0 0 468 165" role="img" aria-label="Decorative cluster of translucent orange leaves in the lower right corner">
    <defs>
      <radialGradient id="leafGlow" cx="0.72" cy="0.95" r="0.8">
        <stop offset="0" stop-color="#ff8a2a" stop-opacity="0.85"/>
        <stop offset="0.55" stop-color="#ffa860" stop-opacity="0.6"/>
        <stop offset="1" stop-color="#ffd2a8" stop-opacity="0"/>
      </radialGradient>
    </defs>
    <rect x="0" y="0" width="468" height="165" fill="url(#leafGlow)"/>
  </svg>

  <footer class="footer-address">Dane Holloway Naturopath Shop 3042c, 451 Marrow Lane, Sydney 2000</footer>
</div>
</body>
</html>
```